Technical audit needs a report template

As our company runs various technical audits, we also provide findings on paper, online or in Powerpoint. For this reason we need an identity pack, which includes business cards, complimentary cards, letterhead and the likes.

Who would be up to create this stationery pack for us? We hope to receive a style for these documents, that look professional and can be easily extended.
Updates

Project Deadline Extended Reason: I would like to provide the opportunity to friended designers to submit their designs too! Added Sunday, October 9, 2016

Target Market(s)

Start-ups, scale-ups and investors

Industry/Entity Type

Investment

Contact Information for Business Card

Street: Kastelenhofweg 41
Postcode: 3614KT
City: Utrecht
Country: The Netherlands
Phone: +31 304185926
Cell Phone: +31 6 57193840
email: jorien@velmoraxis.example
website: https://velmoraxis.example

Requirements
Must have
• I don't have inspiration, should just be a slick design based on the logo provided.
Nice to have
• Logo could be on the back of the card?
Should not have
• Should not use different colours then the logo, or at least fit the colour scheme.

```html
<!DOCTYPE html>
<html lang="en">
<head>
<meta charset="utf-8">
<title>Velmoraxis – Business Cards</title>
<link rel="stylesheet" href="https://fonts.googleapis.com/css2?family=Open+Sans:wght@400;600;700&display=swap">
<style>
  :root {
    --backdrop: #4a423d;
    --card: #141516;
    --card-edge: #0b0b0c;
    --accent: #2a9fc7;
    --accent-dark: #1d6f8f;
    --ink: #f2f2f2;
    --muted: #9a9a9a;
  }
  * { box-sizing: border-box; margin: 0; padding: 0; }
  html, body { width: 1200px; height: 864px; overflow: hidden; }
  body {
    background: var(--backdrop);
    font-family: "Open Sans", Arial, sans-serif;
    position: relative;
  }
  .card {
    position: absolute;
    width: 540px;
    height: 310px;
    background: var(--card);
    border-radius: 4px;
    box-shadow: 0 14px 30px rgba(0,0,0,.45);
    color: var(--ink);
  }
  .card--front { left: 60px; top: 90px; }
  .card--back { left: 600px; top: 460px; }

  .brand { display: flex; align-items: center; gap: 14px; }
  .brand__mark { width: 46px; height: 46px; background: var(--accent); flex: none; }
  .brand__name { font-weight: 700; font-size: 34px; letter-spacing: 1px; color: var(--ink); }

  .card--front .brand { position: absolute; left: 120px; top: 100px; }
  .card--front .website {
    position: absolute; left: 0; right: 0; top: 196px; text-align: center;
    font-size: 13px; letter-spacing: 5px; color: var(--muted);
  }

  .card--back .brand { position: absolute; right: 34px; top: 70px; gap: 10px; }
  .card--back .brand__mark { width: 34px; height: 34px; }
  .card--back .brand__name { font-size: 24px; }

  .holder { position: absolute; left: 34px; top: 92px; }
  .holder__name { color: var(--accent); font-weight: 700; font-size: 17px; letter-spacing: .5px; }
  .holder__role { font-size: 14px; margin-top: 1px; }

  .contacts { position: absolute; left: 34px; top: 142px; list-style: none; font-size: 12.5px; }
  .contacts li { display: flex; align-items: center; gap: 8px; height: 21px; }
  .contacts svg { width: 12px; height: 12px; fill: var(--accent); flex: none; }

  .divider { position: absolute; left: 0; top: 0; width: 540px; height: 310px; pointer-events: none; }

  .address {
    position: absolute; right: 34px; bottom: 22px; text-align: right;
    font-size: 13px; line-height: 20px;
  }
  .address .website { letter-spacing: 3px; }
</style>
</head>
<body>

<section class="card card--front" aria-label="Business card front">
  <div class="brand">
    <span class="brand__mark"></span>
    <span class="brand__name">VELMORAXIS</span>
  </div>
  <p class="website">velmoraxis.example</p>
</section>

<section class="card card--back" aria-label="Business card back">
  <div class="holder">
    <p class="holder__name">JORIEN VOS</p>
    <p class="holder__role">President</p>
  </div>

  <svg class="divider" viewBox="0 0 540 310" aria-hidden="true">
    <line x1="100" y1="132" x2="470" y2="232" stroke="#f2f2f2" stroke-width="1.2"/>
  </svg>

  <ul class="contacts">
    <li>
      <svg viewBox="0 0 12 12"><path d="M1 3c0-1 1-2 2-2h6c1 0 2 1 2 2v1H8V3H4v1H1zM2 5h8l1 6H1z"/></svg>
      +31 304185926
    </li>
    <li>
      <svg viewBox="0 0 12 12"><path d="M3 0h6v12H3zM4 1.5v7.5h4V1.5z"/></svg>
      +31 6 57193840
    </li>
    <li>
      <svg viewBox="0 0 12 12"><path d="M3 0h6v4H3zM1 4h10v6H1zM3 10h6v2H3z"/></svg>
      +31 304185927
    </li>
    <li>
      <svg viewBox="0 0 12 12"><path d="M0 2h12v1L6 7 0 3zM0 4.5l6 4 6-4V10H0z"/></svg>
      jorien@velmoraxis.example
    </li>
  </ul>

  <div class="brand">
    <span class="brand__mark"></span>
    <span class="brand__name">VELMORAXIS</span>
  </div>

  <address class="address" style="font-style:normal">
    Kastelenhofweg 41<br>
    3614KT Utrecht<br>
    <span class="website">velmoraxis.example</span>
  </address>
</section>

</body>
</html>
```